BrivoLane Ute.

I want the full logo on one side. And the other side the card if right Ralf the logo the left half orange like the car in the logo color with Danielle R Morrow
Founder and CEO
Email symbol then dmorrow@brivolaneute.com
Www symbol. Then Brivolaneute.com
Phone symbol then 413-926-BRIV
The very bottom would like Brivo Lane Ute is a division of Harmond Vistas. LLC

```html
<!DOCTYPE html>
<html lang="en">
<head>
<meta charset="utf-8">
<title>Brivo Lane Ute – Business Card</title>
<link rel="stylesheet" href="https://fonts.googleapis.com/css2?family=Montserrat:wght@600;700&family=Overpass:wght@400;500&display=swap">
<style>
  :root {
    --bg: #dcdcdc;
    --paper: #f4f5f8;
    --paper-cool: #e3e5ec;
    --orange: #d08a22;
    --orange-deep: #b8741f;
    --brown: #3a2814;
    --ink: #1f1a14;
    --white: #ffffff;
  }
  * { box-sizing: border-box; margin: 0; padding: 0; }
  html, body {
    width: 1200px; height: 1200px; overflow: hidden;
    background: var(--bg);
  }
  .sheet {
    position: relative; width: 1200px; height: 1200px;
  }
  .card {
    position: absolute; left: 120px; width: 960px; height: 549px;
    overflow: hidden;
    box-shadow: 0 8px 24px rgba(0,0,0,.12);
  }
  .card--front { top: 40px; background: var(--paper); }
  .card--back  { top: 621px; background: var(--paper-cool); }

  /* front */
  .rule {
    position: absolute; height: 4px; background: var(--orange);
    border-radius: 2px;
  }
  .rule--top { top: 42px; left: 60px; right: 60px; }
  .rule--bottom { bottom: 42px; left: 60px; right: 60px; }

  .brand {
    position: absolute; display: flex; align-items: center; gap: 18px;
    font-family: "Montserrat", sans-serif; font-weight: 700;
    color: var(--brown); white-space: nowrap;
  }
  .brand__dot {
    border-radius: 50%; background: var(--orange); flex: none;
  }
  .card--front .brand {
    left: 50%; top: 50%; transform: translate(-50%, -50%);
    font-size: 64px;
  }
  .card--front .brand__dot { width: 62px; height: 62px; }

  /* back */
  .panel {
    position: absolute; left: 0; top: 0; bottom: 0; width: 420px;
    background: linear-gradient(180deg, var(--orange) 0%, var(--orange-deep) 100%);
    clip-path: polygon(0 0, 100% 0, 100% 40%, 92% 40%, 92% 100%, 0 100%);
  }
  .nameplate {
    position: absolute; left: 70px; top: 80px; width: 430px; height: 104px;
    background: var(--brown); color: var(--white);
    font-family: "Montserrat", sans-serif;
    padding: 18px 30px 0 40px;
  }
  .nameplate__name { font-size: 32px; font-weight: 700; letter-spacing: .3px; }
  .nameplate__title {
    font-size: 22px; font-weight: 600; text-align: right; margin-top: 4px;
    padding-right: 70px;
  }
  .contacts {
    position: absolute; left: 20px; top: 250px; width: 400px;
    list-style: none;
    font-family: "Overpass", sans-serif; font-size: 21px; color: var(--ink);
  }
  .contacts li {
    display: flex; justify-content: flex-end; align-items: center;
    height: 40px; margin-bottom: 30px; gap: 16px;
  }
  .contacts .icon {
    width: 36px; height: 36px; border-radius: 50%;
    background: var(--paper-cool); border: 2px solid var(--white);
    display: flex; align-items: center; justify-content: center;
    flex: none; transform: translateX(4px);
  }
  .contacts .icon svg { width: 20px; height: 20px; }

  .card--back .brand {
    left: 660px; top: 235px; transform: translate(-50%, -50%);
    font-size: 40px; gap: 12px;
  }
  .card--back .brand__dot { width: 38px; height: 38px; }
  .division {
    position: absolute; left: 660px; top: 440px; transform: translateX(-50%);
    width: 340px; text-align: center;
    font-family: "Overpass", sans-serif; font-size: 21px; line-height: 1.3;
    color: var(--ink);
  }
  .edge-strip {
    position: absolute; right: 0; top: 0; width: 60px; height: 549px;
  }
</style>
</head>
<body>
<main class="sheet">

  <section class="card card--front" aria-label="Card front">
    <div class="rule rule--top"></div>
    <div class="brand">
      <span class="brand__dot"></span>
      <span class="brand__name">Brivo Lane Ute</span>
    </div>
    <div class="rule rule--bottom"></div>
  </section>

  <section class="card card--back" aria-label="Card back">
    <div class="panel"></div>
    <div class="nameplate">
      <p class="nameplate__name">Danielle R Morrow</p>
      <p class="nameplate__title">Founder &amp; CEO</p>
    </div>
    <ul class="contacts">
      <li>
        <span>dmorrow@brivolaneute.com</span>
        <span class="icon">
          <svg viewBox="0 0 24 24" fill="none" stroke="#b8741f" stroke-width="2"><rect x="3" y="6" width="18" height="12" rx="1"/><path d="M3 7l9 6 9-6"/></svg>
        </span>
      </li>
      <li>
        <span>Brivolaneute.com</span>
        <span class="icon">
          <svg viewBox="0 0 24 24" fill="none" stroke="#b8741f" stroke-width="1.8"><circle cx="12" cy="12" r="9"/><path d="M3 12h18M12 3c3 3 3 15 0 18M12 3c-3 3-3 15 0 18"/></svg>
        </span>
      </li>
      <li>
        <span>413-926-BRIV</span>
        <span class="icon">
          <svg viewBox="0 0 24 24" fill="#b8741f"><path d="M6.6 10.8a15 15 0 006.6 6.6l2.2-2.2a1 1 0 011-.25 11.4 11.4 0 003.6.6 1 1 0 011 1V20a1 1 0 01-1 1A17 17 0 013 4a1 1 0 011-1h3.5a1 1 0 011 1c0 1.25.2 2.45.6 3.6a1 1 0 01-.25 1z"/></svg>
        </span>
      </li>
    </ul>

    <div class="brand">
      <span class="brand__dot"></span>
      <span class="brand__name">Brivo Lane Ute</span>
    </div>
    <p class="division">Brivo Lane Ute is a division of Harmond Vistas. LLC</p>

    <svg class="edge-strip" viewBox="0 0 60 549" aria-hidden="true">
      <rect width="60" height="549" fill="#3a2814"/>
      <circle cx="40" cy="80" r="34" fill="#b8741f" opacity=".7"/>
      <circle cx="40" cy="170" r="38" fill="#d08a22" opacity=".85"/>
      <circle cx="40" cy="270" r="42" fill="#e0a85a" opacity=".7"/>
      <circle cx="40" cy="370" r="38" fill="#d08a22" opacity=".85"/>
      <circle cx="40" cy="460" r="34" fill="#b8741f" opacity=".7"/>
    </svg>
  </section>

</main>
</body>
</html>
```